International MultiIndustry Team Coaching Site

Hello Designers,
We need a redesign of the pages attached.
The design must be engaging and modern, with a focus on the user experience, particularly for the "observations" page. Because this is the main page of the website. It is to be used on a 10'' tablet or desktop, to record observations on the fly, so it must be intuitive and efficient.
The positioning of the metrics and observations and etc, are just a reference. you can switch it up if you feel there is a better way (PLEASE DO ;) ).

There are many categories (color coded with borders in the example hpt_6_observations.jpg) and observation metrics within each category. This is the Key page, because it is the One with the most interactions.

The user should know when it has selected a category (there should be some visual hint) and the different metric widgets should be accounted for.
There are 3: The time widget at the end, numerical widgets (recording more or less numbers), and boolean ones (selected or not).

For the numerical widgets, we show plus and minus characters, but you can change this, being creative, keeping in mind that it must work well on a mobile device and desktop, and must be intuitive and quick.

Set your creativity free with the login screen , home screen, categories secret, events screen, journaling and observations screen .

We would like the site/mobile version to have a very modern look. Something that would be found in very popular and user friendly apps.

***** The events, journaling, category and home screens are getting 2 much attention , please focus also on the observations screen *******
Imagine you are a psychologist tasked with observing the behaviour of teenagers during group work. And you have a tablet on which to record what you observe. Now imagine you need to observe during 3 classes: Biology, Math, Physics (these are events). For each class (event) you will have to record observations in 3 categories: Social Interaction, Leadership, Communication (these are categories).
Example of the metrics (these are observations) for Leadership:
" the teenager direct other colleagues" (boolean widget),
"the teenager speaks more than everyone else" (boolean widget)
"the teenager interrupts colleagues speaking" (number widget)
"the work took hh:mm" (time widget)

The observations screen can have any shape and form you think of. It doesn't need to be that single column with yes and nos, or that double column with the squared cards.
thank you.

Hope that was useful intel :)
Available for any questions you might have.
Good luck :)

Target Market(s)

Enterprise teams

Number of Pages Required

5+ page

Font styles to use
Sans Serif

Requirements
Must have
• Modern design

```html
<!DOCTYPE html>
<html lang="en">
<head>
<meta charset="UTF-8">
<title>Grass Team – Observations</title>
<link href="https://fonts.googleapis.com/css2?family=Poppins:wght@400;500;600&family=Roboto:wght@700&display=swap" rel="stylesheet">
<style>
  :root{
    --ink:#111318;
    --muted:#4a4f5a;
    --card:#ffffff;
    --field:#f5f6fa;
    --chip-border:#dfe2e8;
    --accent:#5588c4;
    --avatar:#4f86c6;
    --toggle-dot:#c2456f;
    --bg-a:#d3e6fb;
    --bg-b:#e4e4f8;
    --bg-c:#f4f6fb;
  }
  *{box-sizing:border-box;margin:0;padding:0}
  html,body{width:1200px;height:800px;overflow:hidden}
  body{
    position:relative;
    font-family:"Poppins",sans-serif;
    color:var(--ink);
    background:
      radial-gradient(ellipse 520px 300px at 300px 40px,var(--bg-a),transparent 70%),
      radial-gradient(ellipse 600px 400px at 820px 120px,var(--bg-b),transparent 70%),
      radial-gradient(ellipse 500px 400px at 1150px 560px,#e6e8f8,transparent 70%),
      var(--bg-c);
  }
  .brand{position:absolute;left:28px;top:22px;display:flex;align-items:center;gap:8px}
  .brand-square{width:30px;height:30px;border-radius:6px;background:var(--avatar)}
  .brand-name{font-weight:600;font-size:21px;letter-spacing:.3px}
  .theme-toggle{position:absolute;left:972px;top:25px;width:59px;height:26px;border-radius:13px;background:#fff;box-shadow:0 1px 4px rgba(0,0,0,.06)}
  .theme-toggle svg{position:absolute;left:8px;top:5px}
  .theme-toggle .dot{position:absolute;right:4px;top:2px;width:22px;height:22px;border-radius:50%;background:var(--toggle-dot)}
  .user{position:absolute;left:1045px;top:17px;display:flex;align-items:center;gap:10px}
  .avatar{width:41px;height:41px;border-radius:50%;background:var(--avatar);border:3px solid #fff;color:#fff;font-weight:600;font-size:19px;display:flex;align-items:center;justify-content:center;box-shadow:0 1px 4px rgba(0,0,0,.08)}
  .user-name{font-weight:600;font-size:13.5px}
  .page-head{position:absolute;left:28px;top:84px;display:flex;align-items:center;gap:26px}
  .page-title{font-weight:500;font-size:23px}
  .observe-card{position:absolute;left:236px;top:155px;width:730px;height:502px;border-radius:21px;background:var(--card);box-shadow:0 14px 30px rgba(80,90,110,.14);padding:51px 41px 0}
  .prompt{font-weight:500;font-size:16px;margin-bottom:11px}
  .note-field{display:block;width:647px;height:129px;border:none;border-radius:7px;background:var(--field);resize:none;font:inherit}
  .tags{margin-top:14px;display:flex;flex-direction:column;gap:8px}
  .tag-row{display:flex;gap:6px}
  .tag{height:35px;border:1.5px solid var(--chip-border);border-radius:6px;background:#fff;font-family:"Poppins",sans-serif;font-size:12.5px;color:var(--muted);display:flex;align-items:center;justify-content:center}
  .save-btn{position:absolute;left:482px;top:409px;width:206px;height:47px;border:none;border-radius:6px;background:var(--accent);color:#fff;font-family:"Roboto",sans-serif;font-weight:700;font-size:12px;letter-spacing:.3px}
</style>
</head>
<body>
  <header>
    <div class="brand"><span class="brand-square"></span><span class="brand-name">LOGO</span></div>
    <div class="theme-toggle">
      <svg width="16" height="16" viewBox="0 0 16 16" fill="none" stroke="#111" stroke-width="1.3" stroke-linecap="round">
        <circle cx="8" cy="8" r="3"/>
        <path d="M8 1v1.6M8 13.4V15M1 8h1.6M13.4 8H15M3 3l1.1 1.1M11.9 11.9L13 13M3 13l1.1-1.1M11.9 4.1L13 3"/>
      </svg>
      <span class="dot"></span>
    </div>
    <div class="user">
      <div class="avatar">N</div>
      <span class="user-name">Hi Marlo</span>
      <svg width="10" height="6" viewBox="0 0 10 6" fill="none" stroke="#555" stroke-width="1.3"><path d="M1 1l4 4 4-4"/></svg>
    </div>
  </header>

  <div class="page-head">
    <svg width="10" height="14" viewBox="0 0 10 14" fill="none" stroke="#111" stroke-width="2" stroke-linecap="round"><path d="M7 2L2 7l5 5"/></svg>
    <h1 class="page-title">Grass Team</h1>
  </div>

  <main class="observe-card">
    <p class="prompt">Welcome! How are you? What are you observing,today?</p>
    <textarea class="note-field" aria-label="Observation notes"></textarea>
    <div class="tags">
      <div class="tag-row">
        <span class="tag" style="width:105px">Collaboration</span>
        <span class="tag" style="width:142px">Communication</span>
        <span class="tag" style="width:177px">Openness &amp; Ownership</span>
        <span class="tag" style="width:167px">Situational Awarness</span>
      </div>
      <div class="tag-row">
        <span class="tag" style="width:105px">Visualization</span>
        <span class="tag" style="width:82px;margin-left:2px">Limit WIP</span>
        <span class="tag" style="width:105px">Manage Flow</span>
        <span class="tag" style="width:177px">Make Policies Explicit</span>
      </div>
    </div>
    <button class="save-btn">SAVE TEAM INFORMATION</button>
  </main>
</body>
</html>
```